QM Lanterns Business Card

Need a professional but with a touch of unique looking Business Card for my staff.

Target Market(s)

Corporate

Industry/Entity Type

Business

Requirements
Must have
• 40mm height

```html
<!DOCTYPE html>
<html lang="en">
<head>
<meta charset="utf-8">
<title>QM Lanterns Business Card</title>
<link rel="stylesheet" href="https://fonts.googleapis.com/css2?family=Share+Tech+Mono&display=swap">
<style>
  :root {
    --backdrop: #0e0f0f;
    --card: #353535;
    --teal: #17a6a8;
    --teal-dim: #2c6d6e;
    --ink-light: #d8d8d8;
    --ink-mid: #8c8c8c;
    --band-light: #9a9a9a;
    --band-dark: #4a4a4a;
  }
  * { margin: 0; padding: 0; box-sizing: border-box; }
  html, body { width: 1200px; height: 900px; overflow: hidden; background: var(--backdrop); }
  body { font-family: "Share Tech Mono", monospace; position: relative; }

  .card {
    position: absolute; left: 20px; top: 66px; width: 1160px; height: 778px;
    background: var(--card);
    border: 6px solid var(--teal);
    box-shadow: inset 0 -14px 0 -8px #6b6b6b;
  }

  .decor-band {
    position: absolute; left: 26px; top: 84px; width: 584px; height: 72px;
    background: linear-gradient(90deg, var(--band-light), var(--band-dark));
  }

  .brand-name {
    position: absolute; left: 72px; top: 296px;
    font-size: 64px; line-height: 1; color: var(--ink-light); letter-spacing: -1px;
    white-space: nowrap;
  }

  .frames { position: absolute; left: 546px; top: 256px; display: flex; gap: 10px; }
  .frame {
    width: 196px; height: 160px;
    border: 4px solid var(--teal-dim);
    border-radius: 6px;
    box-shadow: 0 12px 0 -6px #4a4a4a;
  }

  .person { position: absolute; left: 70px; top: 620px; width: 490px; text-align: center; }
  .person-name { font-size: 44px; color: var(--teal); line-height: 1.1; letter-spacing: -1px; }
  .person-title { font-size: 24px; color: var(--ink-mid); margin-top: 6px; }

  .contact { position: absolute; left: 656px; top: 628px; font-size: 22px; color: var(--ink-mid); }
  .contact-row { position: absolute; white-space: nowrap; }
  .contact-label { color: var(--teal); margin-right: 12px; }
</style>
</head>
<body>
  <div class="card"></div>

  <div class="decor-band" role="img" aria-label="Decorative horizontal stripes with dotted diagonal lines"></div>

  <p class="brand-name">QM Lanterns</p>

  <div class="frames">
    <div class="frame"></div>
    <div class="frame"></div>
    <div class="frame"></div>
  </div>

  <div class="person">
    <p class="person-name">your name goes here</p>
    <p class="person-title">Senior Consultant</p>
  </div>

  <div class="contact">
    <p class="contact-row" style="left:0; top:0;"><span class="contact-label">t</span>0123 456 789 <span class="contact-label" style="margin-left:22px;">f</span>0123 456 790</p>
    <p class="contact-row" style="left:32px; top:34px;"><span class="contact-label">e</span>info@qmlanterns.example</p>
    <p class="contact-row" style="left:86px; top:66px;"><span class="contact-label">w</span>www.qmlanterns.example</p>
    <p class="contact-row" style="left:96px; top:100px;"><span class="contact-label">a</span>12 Harbour Road, Westfield</p>
    <p class="contact-row" style="left:144px; top:134px;">Northshire NS1 2AB</p>
  </div>
</body>
</html>
```